Professional Commercial Cleaning Business needing fresh professional designs for stationary

Need highly professional templates to make our commercial presentations, proposals and tenders standout from the crowd.

We provide cleaning services to large multi national companies. We need to look as professional as our clients and partners.

Needed:
- Word Templates, Cover and main pages
- Power point Templates, Cover and main pages
- Letter Head template
- Header template
- Footer template

Reason: Still waiting on other designed from different designers.

Target Market(s)

Large multi-national companies

Industry/Entity Type

Commercial

Font styles to use
Sans Serif

Colors
3276b5
abd036
cfdeed
85abd2
eaf2ce

Requirements
Must have
• Please see brief for what we need specifically.
• Show our logo
• Use QAB logos

```html
<!DOCTYPE html>
<html lang="en">
<head>
<meta charset="utf-8">
<title>Brightway Cleaning Services – Word Template</title>
<link href="https://fonts.googleapis.com/css2?family=Arimo:wght@400;700&family=Oswald:wght@400&family=Raleway:wght@500;600&display=swap" rel="stylesheet">
<style>
  :root{
    --brand-blue:#3276b5;
    --brand-green:#abd036;
    --pale-blue:#cfdeed;
    --mid-blue:#85abd2;
    --pale-green:#eaf2ce;
    --backdrop:#b4b4b4;
    --paper:#ffffff;
    --ink:#222222;
    --ink-soft:#555555;
  }
  *{margin:0;padding:0;box-sizing:border-box}
  html,body{width:1200px;height:900px;overflow:hidden}
  body{background:var(--backdrop);position:relative;font-family:"Arimo",Arial,sans-serif}
  .showcase-title,.page-label{position:absolute;color:#fff;font-family:"Raleway",sans-serif;font-weight:600;text-align:center;transform:translateX(-50%)}
  .showcase-title{left:606px;top:42px;font-size:48px}
  .page-label{font-size:34px;line-height:1}
  .page-label small{display:block;font-size:16px;margin-top:4px}
  .label-letterhead{left:366px;top:806px}
  .label-cover{left:835px;top:810px}

  .letterhead,.cover{position:absolute;background:var(--paper)}
  .letterhead{left:146px;top:148px;width:438px;height:618px}
  .cover{left:616px;top:150px;width:434px;height:614px}

  .lh-header{position:absolute;left:0;top:0}
  .lh-brand{position:absolute;left:0;width:100%;top:62px;text-align:center;font-weight:700;font-size:14px;color:var(--brand-blue)}
  .lh-brand .brand-dot{display:inline-block;width:9px;height:9px;border-radius:50%;background:var(--brand-green);margin-right:5px;vertical-align:0}
  .lh-recipient{position:absolute;right:32px;top:76px;text-align:right;font-size:9px;line-height:12.5px;color:var(--ink)}
  .lh-salutation{position:absolute;left:30px;top:121px;font-size:10px;font-weight:700;color:var(--ink-soft)}
  .lh-body{position:absolute;left:30px;width:378px;font-size:7px;line-height:14.7px;color:var(--ink)}
  .lh-body.p1{top:158px}
  .lh-body.p2{top:320px}
  .lh-closing{position:absolute;left:30px;top:478px;font-size:7.5px;color:var(--ink-soft)}
  .lh-footer{position:absolute;left:0;bottom:0}

  .cover-photo,.cover-block{position:absolute}
  .photo-atrium{left:26px;top:24px;width:118px;height:256px;background:linear-gradient(160deg,#5a6f86,#1e2b3a 70%,#3b4a5a)}
  .brand-panel{left:152px;top:24px;width:257px;height:256px;background:var(--pale-blue);display:flex;align-items:center;justify-content:center}
  .brand-panel .brand-name{font-weight:700;font-size:27px;color:var(--brand-blue);line-height:1}
  .brand-panel .brand-dot{display:inline-block;width:22px;height:22px;border-radius:50%;background:var(--brand-green);margin-right:10px;vertical-align:-2px}
  .headline-band{left:26px;top:290px;width:254px;height:143px;background:linear-gradient(90deg,var(--brand-blue) 0%,var(--brand-blue) 55%,var(--mid-blue) 70%,#dfeab0 90%,#e4ecbf 100%);display:flex;align-items:center;padding-left:32px}
  .headline-band h1{font-family:"Raleway",sans-serif;font-weight:500;font-size:34px;color:#fff}
  .accent-panel{left:288px;top:290px;width:121px;height:143px;background:var(--pale-green)}
  .contact-panel{left:26px;top:444px;width:118px;height:142px;background:#7fa4cd;padding:26px 5px 0 5px;font-family:"Oswald",sans-serif;font-size:6.4px;line-height:10px;color:#fff;text-transform:uppercase}
  .contact-panel p{margin-bottom:8px}
  .photo-building{left:152px;top:444px;width:257px;height:142px;background:linear-gradient(180deg,#2a3552 0%,#5a6a8a 45%,#6e8a5a 70%,#8e9a8e 100%)}
</style>
</head>
<body>
  <h2 class="showcase-title">Word Template</h2>

  <section class="letterhead" aria-label="Letterhead">
    <svg class="lh-header" width="438" height="70" viewBox="0 0 438 70">
      <path d="M0,0H438V46L300,50C268,52 262,64 219,64C176,64 170,52 138,50L0,46Z" fill="#3276b5"/>
      <path d="M0,49L138,53C170,55 176,67 219,67C262,67 268,55 300,53L438,49" fill="none" stroke="#85abd2" stroke-width="1.5"/>
    </svg>
    <div class="lh-brand"><span class="brand-dot"></span>Brightway</div>

    <address class="lh-recipient" style="font-style:normal">
      Nora Whitfield<br>Meridian Holdings<br>Level 7 18 Harbour Rd<br>Eastvale NSW 2150<br>Australia
    </address>
    <p class="lh-salutation">Dear Ms. Whitfield</p>
    <p class="lh-body p1">Lorem ipsum dolor sit amet, consectetur adipiscing elit. Vestibulum adipiscing felis ac tortor consectetur feugiat. Etiam malesuada sodales eros ut ornare. Sed lorem eros, mattis id pretium ut, faucibus sit amet quam. Nullam consectetur ultricies ipsum, fringilla porttitor erat ornare at. Sed sit amet dui vel sapien ultrices vulputate. In hac habitasse platea dictumst. Nam est nisi, rhoncus at sagittis a, porttitor adipiscing nulla. Vivamus placerat felis ultrices quam iaculis eget dignissim felis egestas. Integer nec molestie lorem. Sed odio tellus, vulputate sed laoreet non, vulputate id justo. Etiam suscipit, odio vel auctor dictum, felis turpis ullamcorper neque, quis sodales risus metus in magna. Morbi pellentesque justo et quam laoreet facilisis. Aenean placerat, urna ornare aliquet tincidunt, lorem justo molestie ligula, id placerat est metus nec lectus. Nullam eu ipsum quis turpis tristique iaculis rutrum nec nibh. Phasellus risus eros, semper sit amet faucibus sit amet, laoreet et neque. Donec eros sem, viverra dictum faucibus quis, ullamcorper tincidunt nulla.</p>
    <p class="lh-body p2">Aenean ut congue tellus. Class aptent taciti sociosqu ad litora torquent per conubia nostra, per inceptos himenaeos. Sed facilisis, velit tincidunt pharetra fermentum, urna tortor iaculis erat, vitae sollicitudin leo mauris quis mi. Cras malesuada sem ac ipsum sagittis ultrices. Mauris fermentum porttitor nisi, eu facilisis lorem consectetur et. Suspendisse est elit, scelerisque ac euismod id, scelerisque viverra odio. Nullam scelerisque metus in eros semper congue. Fusce a fermentum est. Ut ac leo dolor. Quisque dignissim mauris a neque luctus pretium ultrices risus sagittis. Aenean quam massa, rutrum ac hendrerit eu, interdum eu nulla. Curabitur a velit mauris, sed porta eros. Cras id egestas sapien. Proin non metus eget felis eleifend adipiscing. Nunc malesuada pharetra blandit.</p>
    <p class="lh-closing">Your sincerely</p>

    <svg class="lh-footer" width="438" height="48" viewBox="0 0 438 48">
      <rect x="0" y="0" width="438" height="2" fill="#3276b5"/>
      <rect x="0" y="5" width="438" height="1.5" fill="#85abd2"/>
      <rect x="0" y="10" width="438" height="38" fill="#3276b5"/>
      <path d="M100,6H338L330,30H108Z" fill="#ffffff"/>
      <g class="cert-badges">
        <rect x="122" y="9" width="42" height="18" rx="2" fill="#d9353b"/>
        <rect x="172" y="9" width="42" height="18" rx="2" fill="#4a9a3c"/>
        <rect x="224" y="9" width="42" height="18" rx="2" fill="#2f5fa8"/>
        <rect x="274" y="9" width="42" height="18" rx="2" fill="#4a9a3c"/>
      </g>
    </svg>
  </section>
  <p class="page-label label-letterhead">Letterhead<small>(Header and Footer)</small></p>

  <section class="cover" aria-label="Document cover">
    <div class="cover-photo photo-atrium" role="img" aria-label="Photo of a modern office atrium with lounge seating"></div>
    <div class="cover-block brand-panel"><span class="brand-name"><span class="brand-dot"></span>Brightway</span></div>
    <div class="cover-block headline-band"><h1>Headline</h1></div>
    <div class="cover-block accent-panel"></div>
    <div class="cover-block contact-panel">
      <p>Office hours: 9am - 5pm<br>Phone: 02 5550 1847<br>24 hours: 1300 555 214</p>
      <p>Head office<br>9/41 Orchard St<br>Westbrook NSW 2071</p>
      <p>www.brightwaycleaning.example</p>
    </div>
    <div class="cover-photo photo-building" role="img" aria-label="Photo of a modern apartment building with landscaped courtyard"></div>
  </section>
  <p class="page-label label-cover">Cover</p>
</body>
</html>
```